Very Simple/Minimal Business Card Design Project

The company operates in the industrial maritime infrastructure sector in Brazil. You can find more information on our website www.navortek.com.br WE NEED TO LOOK POWERFUL AND SERIOUS
I have attached a copy of the old cards. We would like something more professional / industrial / sexy that also includes the position.

The card can be double sided or not. We would like you to propose as many options.

Thank you
Updates

Many thanks, do let me know if you have any questions. I am under a lot of time pressure to try and have them printed over the next days or so.

Please could you use the following information

for the address: Rua Tapiraçu, 417 - Centro, Rio de Janeiro, 20034-118, Brasil

for the mobile: +55 21 8237 9412
for the landline: +55 21 4096 3578

and position:  Diretor Geral

Thakn you

Target Market(s)

Shipowners, bankers, industrial companies

Industry/Entity Type

Industrial

Requirements
Must have
• POWERFUL
SERIOUS
SOLID
BIG CORPORATION

```html
<!DOCTYPE html>
<html lang="pt-BR">
<head>
<meta charset="utf-8">
<title>Navortek – Cartão de Visita</title>
<link href="https://fonts.googleapis.com/css2?family=Roboto:wght@400;700&display=swap" rel="stylesheet">
<style>
  :root {
    --stage: #6d6e70;
    --navy-deep: #2c2b5e;
    --navy-glow: #1a3079;
    --navy-text: #1f2a6b;
    --green: #1f9e48;
    --white: #ffffff;
    --paper-edge: #ececec;
    --rule: #8a8c96;
  }
  * { box-sizing: border-box; margin: 0; padding: 0; }
  html, body { width: 1200px; height: 396px; overflow: hidden; }
  body {
    background: var(--stage);
    font-family: "Roboto", Arial, sans-serif;
    position: relative;
  }
  .card {
    position: absolute;
    top: 52px;
    height: 293px;
  }
  .card--front {
    left: 89px;
    width: 504px;
    background: radial-gradient(ellipse at 50% 50%, var(--navy-glow) 0%, var(--navy-deep) 75%);
    display: flex;
    align-items: center;
    justify-content: center;
  }
  .card--back {
    left: 625px;
    width: 507px;
    background: radial-gradient(ellipse at 50% 45%, var(--white) 40%, var(--paper-edge) 100%);
    color: var(--navy-text);
  }
  .brand {
    display: flex;
    align-items: center;
    gap: 10px;
    font-weight: 700;
    letter-spacing: 0.5px;
  }
  .brand__mark { display: block; border-radius: 6px; }
  .card--front .brand { font-size: 44px; color: var(--white); }
  .card--front .brand__mark { width: 58px; height: 58px; background: var(--white); }
  .card--back .brand {
    position: absolute; left: 34px; top: 40px;
    font-size: 30px; color: var(--navy-text);
  }
  .card--back .brand__mark { width: 45px; height: 45px; background: var(--green); border-radius: 4px; }
  .holder {
    position: absolute; right: 33px; top: 96px;
    text-align: right;
  }
  .holder__name { font-size: 20px; font-weight: 400; line-height: 22px; }
  .holder__role { font-size: 13px; font-weight: 400; line-height: 16px; margin-top: 1px; }
  .rule {
    position: absolute; left: 34px; top: 137px;
    width: 440px; height: 2px; background: var(--rule);
  }
  .contacts {
    position: absolute; top: 153px;
    list-style: none;
  }
  .contacts--left { left: 34px; }
  .contacts--right { left: 302px; }
  .contacts li {
    display: flex; align-items: center; gap: 7px;
    height: 24px; font-size: 15.5px;
  }
  .contacts li.indent { padding-left: 26px; }
  .icon { width: 19px; height: 19px; flex: none; }
  .icon circle { fill: var(--green); }
  .icon .glyph { fill: none; stroke: var(--white); stroke-width: 1.6; stroke-linecap: round; stroke-linejoin: round; }
  .icon .dot { fill: var(--white); }
</style>
</head>
<body>

<section class="card card--front" aria-label="Frente do cartão">
  <div class="brand"><span class="brand__mark"></span>NAVORTEK</div>
</section>

<section class="card card--back" aria-label="Verso do cartão">
  <div class="brand"><span class="brand__mark"></span>NAVORTEK</div>
  <div class="holder">
    <p class="holder__name">Rafael Montenegro</p>
    <p class="holder__role">Diretor Geral</p>
  </div>
  <div class="rule"></div>

  <ul class="contacts contacts--left">
    <li>
      <svg class="icon" viewBox="0 0 20 20"><circle cx="10" cy="10" r="10"/><rect class="glyph" x="7" y="4.5" width="6" height="11" rx="1"/><circle class="dot" cx="10" cy="13.5" r="0.8" style="fill:#fff"/></svg>
      +55 21 4096 3578
    </li>
    <li>
      <svg class="icon" viewBox="0 0 20 20"><circle cx="10" cy="10" r="10"/><path class="glyph" d="M6 5.5c0 5 3.5 8.5 8.5 8.5l0.5-2-2.5-1-1 1.2c-1.3-.6-2.4-1.7-3-3l1.2-1-1-2.5z"/></svg>
      +55 21 8237 9412
    </li>
    <li>
      <svg class="icon" viewBox="0 0 20 20"><circle cx="10" cy="10" r="10"/><rect class="glyph" x="5" y="6.5" width="10" height="7" rx="0.8"/><path class="glyph" d="M5.3 7l4.7 3.5 4.7-3.5"/></svg>
      rafael@navortek.com.br
    </li>
    <li>
      <svg class="icon" viewBox="0 0 20 20"><circle cx="10" cy="10" r="10"/><path class="glyph" d="M4.5 9a8 8 0 0 1 11 0M6.5 11a5 5 0 0 1 7 0M8.5 13a2 2 0 0 1 3 0"/></svg>
      www.navortek.com.br
    </li>
  </ul>

  <ul class="contacts contacts--right">
    <li>
      <svg class="icon" viewBox="0 0 20 20"><circle cx="10" cy="10" r="10"/><path class="glyph" d="M4.5 10l5.5-5 5.5 5M6.5 8.5v6h7v-6"/></svg>
      Rua Tapiraçu, 417
    </li>
    <li class="indent">Centro</li>
    <li>
      <svg class="icon" viewBox="0 0 20 20"><circle cx="10" cy="10" r="10"/><rect class="glyph" x="5" y="6.5" width="10" height="7" rx="0.8"/><path class="glyph" d="M5.3 7l4.7 3.5 4.7-3.5"/></svg>
      CEP 20034-118
    </li>
    <li>
      <svg class="icon" viewBox="0 0 20 20"><circle cx="10" cy="10" r="10"/><path class="glyph" d="M10 15.5s-4-4-4-7a4 4 0 0 1 8 0c0 3-4 7-4 7z"/><circle cx="10" cy="8.5" r="1.3" style="fill:#fff"/></svg>
      Rio de Janeiro
    </li>
  </ul>
</section>

</body>
</html>
```